Velo 3D Imaging
Simple
Brelmont 3D Dental Imaging, Inc.
218 North Marlow Avenue Suite 4C Harlow Glen, NJ 07921
info@Brelmont3D-example.com
www.Brelmont3D-example.com
Do not need individual names of people on the card. These are to be given to other doctors who would refer to the business to have CT scans done for their patient

```html
<!DOCTYPE html>
<html lang="en">
<head>
<meta charset="utf-8">
<title>Brelmont 3D Dental Imaging – Business Card</title>
<link rel="stylesheet" href="https://fonts.googleapis.com/css2?family=Source+Sans+3:wght@400&display=swap">
<style>
  :root {
    --canvas-bg: #e9e6e2;
    --card-white: #ffffff;
    --brand-blue: #1f5c93;
    --text-blue: #2a6aa6;
    --back-light: #2f6da8;
    --back-dark: #173e6b;
    --back-text: #d9e8f6;
    --shadow: rgba(40, 30, 20, 0.28);
  }
  * { box-sizing: border-box; margin: 0; padding: 0; }
  html, body {
    width: 1200px;
    height: 1030px;
    overflow: hidden;
    background: var(--canvas-bg);
    font-family: "Source Sans 3", Arial, sans-serif;
  }
  .canvas { position: relative; width: 1200px; height: 1030px; }
  .card {
    position: absolute;
    width: 640px;
    height: 366px;
    border-radius: 18px;
    box-shadow: 0 14px 30px var(--shadow);
    overflow: hidden;
  }

  /* Front */
  .card-front { left: 110px; top: 100px; background: var(--card-white); }
  .card-front .edge-tab {
    position: absolute;
    left: 0;
    top: 262px;
    width: 8px;
    height: 64px;
    background: var(--brand-blue);
  }
  .identity {
    position: absolute;
    left: 70px;
    top: 128px;
    display: flex;
    align-items: center;
    gap: 16px;
  }
  .identity .mark-dot {
    width: 54px;
    height: 54px;
    border-radius: 50%;
    background: var(--brand-blue);
    flex: none;
  }
  .identity .name { color: var(--brand-blue); font-weight: 400; line-height: 1; }
  .identity .name-main { display: block; font-size: 46px; letter-spacing: -0.5px; }
  .identity .name-sub { display: block; font-size: 25px; margin-top: 4px; }
  .contact {
    position: absolute;
    left: 70px;
    top: 232px;
    list-style: none;
    color: var(--text-blue);
    font-size: 14px;
    line-height: 19px;
    font-weight: 400;
    white-space: nowrap;
  }

  /* Back */
  .card-back {
    left: 450px;
    top: 560px;
    background: radial-gradient(ellipse at 45% 35%, var(--back-light) 0%, var(--brand-blue) 45%, var(--back-dark) 100%);
    display: flex;
    align-items: center;
    justify-content: center;
  }
  .back-identity { display: flex; align-items: center; gap: 14px; }
  .back-identity .mark-dot {
    width: 44px;
    height: 44px;
    border-radius: 50%;
    background: var(--back-text);
  }
  .back-identity .name {
    color: var(--back-text);
    font-size: 38px;
    font-weight: 400;
    letter-spacing: -0.3px;
  }
</style>
</head>
<body>
<main class="canvas">
  <section class="card card-front" aria-label="Business card front">
    <div class="edge-tab"></div>
    <div class="identity">
      <span class="mark-dot"></span>
      <h1 class="name">
        <span class="name-main">Brelmont 3D</span>
        <span class="name-sub">Dental Imaging, Inc.</span>
      </h1>
    </div>
    <ul class="contact">
      <li>218 North Marlow Avenue Suite 4C</li>
      <li>Harlow Glen, NJ 07921</li>
      <li>P: 856-555-0142 F: 856-555-0187</li>
      <li>E: info@Brelmont3D-example.com W: www.Brelmont3D-example.com</li>
    </ul>
  </section>

  <section class="card card-back" aria-label="Business card back">
    <div class="back-identity">
      <span class="mark-dot"></span>
      <span class="name">Brelmont 3D</span>
    </div>
  </section>
</main>
</body>
</html>
```